Highlight Document Over Image for Slide

We are seeking a graphic designer to overlay a news article on an image that pertains to the article, aiming for a stylish yet professional appearance. Given the limited resources, we encourage you to use your imagination and go beyond what basic tools like PowerPoint can offer.

```html
<!DOCTYPE html>
<html lang="en">
<head>
<meta charset="utf-8">
<title>Introduction or Possession of Contraband Items</title>
<link href="https://fonts.googleapis.com/css2?family=Outfit:wght@400;700;800&display=swap" rel="stylesheet">
<style>
  :root {
    --land-dry: #a8946a;
    --land-built: #8a8373;
    --shore: #7d7a6c;
    --water: #6f6c66;
    --water-deep: #5f5d58;
    --frame-light: #ffffff;
    --frame-mid: #8fb0ea;
    --frame-blue: #1a55c4;
    --card-top: #0a4db2;
    --card-mid: #06285e;
    --card-bottom: #000000;
    --text: #ffffff;
  }
  * { margin: 0; padding: 0; box-sizing: border-box; }
  html, body {
    width: 1200px;
    height: 703px;
    overflow: hidden;
    background: var(--water);
  }
  .slide {
    position: relative;
    width: 1200px;
    height: 703px;
    overflow: hidden;
  }
  .aerial-map {
    position: absolute;
    inset: 0;
    background:
      radial-gradient(ellipse 520px 300px at 230px 250px, var(--land-built) 0%, rgba(138,131,115,0) 100%),
      linear-gradient(172deg, var(--land-dry) 0%, var(--land-built) 42%, var(--shore) 58%, var(--water) 70%, var(--water-deep) 100%);
  }
  .story-frame {
    position: absolute;
    left: 482px;
    top: 147px;
    width: 652px;
    height: 409px;
    border-radius: 0 72px 8px 84px;
    background: linear-gradient(180deg, var(--frame-light) 0%, var(--frame-mid) 45%, var(--frame-blue) 100%);
    padding: 9px 9px 9px 9px;
  }
  .story-card {
    width: 100%;
    height: 100%;
    border-radius: 0 64px 2px 78px;
    background: linear-gradient(180deg, var(--card-top) 0%, var(--card-mid) 45%, var(--card-bottom) 92%);
    padding: 62px 40px 0 61px;
    color: var(--text);
  }
  .story-title {
    font-family: "Outfit", sans-serif;
    font-weight: 800;
    font-size: 34px;
    line-height: 36.5px;
    letter-spacing: 0.2px;
    text-transform: uppercase;
  }
  .story-body {
    margin-top: 40px;
    font-family: "Outfit", sans-serif;
    font-weight: 400;
    font-size: 21.5px;
    line-height: 31px;
  }
</style>
</head>
<body>
  <main class="slide">
    <div class="aerial-map" role="img" aria-label="Aerial map of a waterfront correctional facility with roads, buildings and the bay shoreline"></div>
    <article class="story-frame">
      <div class="story-card">
        <h1 class="story-title">Introduction or Possession<br>of Contraband Items</h1>
        <p class="story-body">Lorem ipsum dolor sit amet, consectetur adipiscing elit, sed do eiusmod tempor incididunt ut labore et dolore magna aliqua. Quis ipsum suspendisse ultrices gravida. Risus commodo viverra maecenas accumsan lacus vel facilisis.</p>
      </div>
    </article>
  </main>
</body>
</html>
```